Convert Design into Adobe Ilustrator (Ai) File - Product Label

Convert the provided Graphic Design into an Adobe Illustrator (Ai) File for a Product Label. This Ai file needs to be fully editable, organised into logical layers and well structured. The text needs to be outlined for printing. This is for a POUCH DESIGN. The pouch dimensions file is attached. We'll share the details for the other side of the pouch if you are interested in accepting this project. Thanks.

Industry/Entity Type

FOOD SUPPLEMENTS

```html
<!DOCTYPE html>
<html lang="en">
<head>
<meta charset="utf-8">
<title>Marine Collagen Complex – Pouch Front</title>
<link rel="stylesheet" href="https://fonts.googleapis.com/css2?family=Tinos:wght@400;700&display=swap">
<style>
  :root {
    --navy: #1a2541;
    --navy-deep: #121b33;
    --gold: #e8c36a;
    --peach: #f2c59a;
    --white: #ffffff;
    --dieline: #1fa9e6;
  }
  * { margin: 0; padding: 0; box-sizing: border-box; }
  html, body {
    width: 877px;
    height: 1200px;
    overflow: hidden;
    background: #ffffff;
  }
  .pouch {
    position: relative;
    width: 877px;
    height: 1200px;
    background: var(--navy);
    border-radius: 16px;
    overflow: hidden;
    font-family: "Tinos", "Times New Roman", serif;
    color: var(--white);
  }
  .wave-field {
    position: absolute;
    left: 0;
    top: 0;
    width: 877px;
    height: 1200px;
  }
  .dielines {
    position: absolute;
    inset: 0;
    width: 877px;
    height: 1200px;
    pointer-events: none;
  }
  .brand-name {
    position: absolute;
    top: 222px;
    left: 93px;
    width: 691px;
    text-align: center;
    font-size: 40px;
    font-weight: 400;
    letter-spacing: 24px;
    padding-left: 24px;
    line-height: 1;
  }
  .brand-rule {
    position: absolute;
    top: 287px;
    left: 93px;
    width: 691px;
    height: 3px;
    background: var(--gold);
  }
  .product-title {
    position: absolute;
    top: 322px;
    left: 87px;
    color: var(--gold);
    font-size: 71px;
    font-weight: 400;
    line-height: 81px;
    letter-spacing: -0.5px;
  }
  .product-subtitle {
    position: absolute;
    top: 622px;
    left: 89px;
    font-size: 34px;
    line-height: 43px;
  }
  .serving-info {
    position: absolute;
    top: 788px;
    left: 89px;
    font-size: 18px;
  }
  .feature-list {
    position: absolute;
    top: 614px;
    left: 494px;
    list-style: none;
  }
  .feature {
    display: flex;
    align-items: center;
    height: 60px;
    margin-bottom: 9px;
  }
  .feature-icon {
    width: 52px;
    height: 52px;
    flex: none;
  }
  .feature-label {
    margin-left: 23px;
    font-size: 19px;
    line-height: 24px;
  }
  .pack-info {
    position: absolute;
    top: 1072px;
    left: 0;
    width: 877px;
    text-align: center;
    font-size: 18px;
    font-weight: 700;
  }
</style>
</head>
<body>
  <main class="pouch">
    <svg class="wave-field" role="img" aria-label="Flowing fine-line wave pattern across the lower part of the pouch" viewBox="0 0 877 1200">
      <defs>
        <linearGradient id="waveTone" x1="0" y1="0" x2="0" y2="1">
          <stop offset="0" stop-color="#1a2541" stop-opacity="0"/>
          <stop offset="1" stop-color="#121b33" stop-opacity="0.85"/>
        </linearGradient>
      </defs>
      <rect x="0" y="760" width="877" height="440" fill="url(#waveTone)"/>
    </svg>

    <svg class="dielines" viewBox="0 0 877 1200" fill="none" stroke="var(--dieline)" stroke-width="1" stroke-dasharray="6 5">
      <line x1="37" y1="0" x2="37" y2="1200"/>
      <line x1="840" y1="0" x2="840" y2="1200"/>
      <line x1="0" y1="116" x2="877" y2="116"/>
      <line x1="0" y1="145" x2="877" y2="145"/>
      <line x1="0" y1="175" x2="877" y2="175"/>
      <line x1="0" y1="946" x2="37" y2="946"/>
      <line x1="840" y1="946" x2="877" y2="946"/>
      <path d="M37 946 C 150 1060, 300 1150, 441 1152 C 600 1150, 740 1060, 840 946"/>
    </svg>

    <h2 class="brand-name">NORTH &amp; TIDE</h2>
    <div class="brand-rule"></div>

    <h1 class="product-title">MARINE<br>COLLAGEN<br>COMPLEX</h1>

    <p class="product-subtitle">Marine Collagen,<br>Vitamin C<br>&amp; Hyaluronic Acid</p>

    <p class="serving-info">30 servings | 13.500mg per serving</p>

    <ul class="feature-list">
      <li class="feature">
        <svg class="feature-icon" viewBox="0 0 52 52" fill="none" stroke="var(--peach)" stroke-width="2" stroke-linecap="round">
          <path d="M8 18 A 22 22 0 0 1 22 5"/>
          <path d="M30 5 A 22 22 0 0 1 44 18"/>
          <path d="M44 34 A 22 22 0 0 1 8 34"/>
          <circle cx="26" cy="4" r="2.5"/>
          <circle cx="4" cy="26" r="2.5"/>
          <circle cx="48" cy="26" r="2.5"/>
          <line x1="26" y1="12" x2="26" y2="44"/>
          <path d="M26 22 Q 20 20 18 26"/>
          <path d="M26 22 Q 32 20 34 26"/>
          <path d="M26 30 Q 20 28 18 34"/>
          <path d="M26 30 Q 32 28 34 34"/>
        </svg>
        <span class="feature-label">Low molecular weight</span>
      </li>
      <li class="feature">
        <svg class="feature-icon" viewBox="0 0 52 52" fill="none" stroke="var(--peach)" stroke-width="2">
          <path d="M26 3 C 20 14, 9 24, 9 35 A 17 16 0 0 0 43 35 C 43 24, 32 14, 26 3 Z"/>
        </svg>
        <span class="feature-label">2000 kDa</span>
      </li>
      <li class="feature">
        <svg class="feature-icon" viewBox="0 0 52 52" fill="none" stroke="var(--peach)" stroke-width="2" stroke-linecap="round">
          <path d="M44 4 C 20 6, 8 18, 12 38 C 30 42, 44 30, 44 4 Z"/>
          <line x1="4" y1="48" x2="30" y2="20"/>
          <path d="M20 30 L 20 20"/>
          <path d="M20 30 L 30 30"/>
        </svg>
        <span class="feature-label">Unflavoured</span>
      </li>
      <li class="feature">
        <svg class="feature-icon" role="img" aria-label="Small wild-caught fish icon" viewBox="0 0 52 52">
          <circle cx="26" cy="26" r="20" fill="var(--peach)" fill-opacity="0.85"/>
        </svg>
        <span class="feature-label">Sourced from<br>wild caught fish</span>
      </li>
    </ul>

    <p class="pack-info">Food Supplement | e 375g</p>
  </main>
</body>
</html>
```